Stationery Design Project - KORVELT-NINE

Presentation Folder
Size: A4
Notepad
Size: 250mm x 140mm
With Compliments Slip
Size: DL
210mm x 99mm
Letterhead
Size: A4 - 210mm x 297mm
Business Cards
Size: 90mm x 55mm

Company is called "KORVELT-NINE"
website: www.korveltnine.com.au (under construction)

Offices: *Perth *Brisbane *Seoul *Hong Kong

If you need any further information please let me know!

Cheers

Lionel

```html
<!DOCTYPE html>
<html lang="en">
<head>
<meta charset="utf-8">
<title>KORVELT-NINE Notepad</title>
<link rel="stylesheet" href="https://fonts.googleapis.com/css2?family=Arimo:wght@400&family=Roboto+Condensed:wght@400;500&display=swap">
<style>
  :root {
    --backdrop: #4b4e52;
    --paper: #ffffff;
    --brand-grey: #6b6f75;
    --brand-square: #8fc6e6;
    --heading-blue: #2a8ab5;
    --ink: #1f1f1f;
    --muted: #8a8a8a;
    --band-blue: #2462b0;
    --ice-light: #e8f3fb;
    --ice-mid: #a9d6f2;
    --ice-deep: #5fb3e6;
  }
  html, body {
    margin: 0;
    padding: 0;
    width: 777px;
    height: 1200px;
    overflow: hidden;
    background: var(--backdrop);
  }
  .canvas {
    position: relative;
    width: 777px;
    height: 1200px;
  }
  .notepad {
    position: absolute;
    left: 75px;
    top: 40px;
    width: 627px;
    height: 1120px;
    background: var(--paper);
    overflow: hidden;
  }
  .brand {
    position: absolute;
    top: 62px;
    left: 0;
    right: 0;
    display: flex;
    justify-content: center;
    align-items: center;
    gap: 14px;
    padding-left: 40px;
  }
  .brand-square {
    width: 54px;
    height: 54px;
    background: var(--brand-square);
  }
  .brand-name {
    font-family: "Arimo", Arial, sans-serif;
    font-weight: 400;
    font-size: 32px;
    letter-spacing: 1px;
    color: var(--brand-grey);
  }
  .cube-artwork {
    position: absolute;
    left: 242px;
    top: 733px;
    width: 385px;
    height: 366px;
    background:
      radial-gradient(ellipse at 60% 40%, var(--ice-deep) 0%, rgba(95,179,230,0) 55%),
      linear-gradient(160deg, var(--ice-light) 0%, var(--ice-mid) 55%, var(--ice-light) 100%);
    -webkit-mask-image: linear-gradient(90deg, transparent 0%, #000 30%);
    mask-image: linear-gradient(90deg, transparent 0%, #000 30%);
  }
  .office {
    position: absolute;
    left: 45px;
    top: 790px;
    width: 260px;
  }
  .office-title {
    margin: 0 0 14px;
    font-family: "Arimo", Arial, sans-serif;
    font-weight: 400;
    font-size: 15px;
    color: var(--heading-blue);
  }
  .office-address {
    margin: 0 0 22px;
    font-family: "Roboto Condensed", "Arial Narrow", sans-serif;
    font-weight: 500;
    font-size: 14px;
    line-height: 20.5px;
    font-style: normal;
    color: var(--ink);
  }
  .contact-list {
    margin: 0 0 24px;
    padding: 0;
    list-style: none;
    font-family: "Roboto Condensed", "Arial Narrow", sans-serif;
    font-weight: 500;
    font-size: 14px;
    line-height: 21.3px;
    color: var(--ink);
  }
  .contact-list li {
    display: flex;
  }
  .contact-label {
    width: 30px;
    text-align: right;
    padding-right: 10px;
    flex: none;
  }
  .tagline {
    margin: 0;
    width: 200px;
    font-family: "Arimo", Arial, sans-serif;
    font-size: 15px;
    line-height: 18.5px;
    color: var(--muted);
  }
  .footer-band {
    position: absolute;
    left: 0;
    right: 0;
    bottom: 0;
    height: 21px;
    background: var(--band-blue);
  }
</style>
</head>
<body>
<div class="canvas">
  <div class="notepad">
    <header class="brand">
      <span class="brand-square"></span>
      <span class="brand-name">KORVELT-NINE</span>
    </header>

    <div class="cube-artwork" role="img" aria-label="Illustration of stacked translucent blue and white 3D cubes"></div>

    <section class="office">
      <h2 class="office-title">PERTH OFFICE</h2>
      <address class="office-address">
        Suite 4, 212 Harlow Street<br>
        Westmere<br>
        Western Australia 6011
      </address>
      <ul class="contact-list">
        <li><span class="contact-label">P |</span><span>+61 (0) 8 5550 1724</span></li>
        <li><span class="contact-label">F |</span><span>+61 (0) 8 5550 1790</span></li>
        <li><span class="contact-label">E |</span><span>info@korveltnine.com.au</span></li>
        <li><span class="contact-label">W |</span><span>http://www.korveltnine.com.au</span></li>
      </ul>
      <p class="tagline">Australia's number one group in health, safety, environmental and quality recruitment.</p>
    </section>

    <div class="footer-band"></div>
  </div>
</div>
</body>
</html>
```